New Carpathian Kosher Billboard

Need to prepare a billboard for a KOSHER supermarket that is under new ownership. The billboard needs to have a good catch phrase such as:

A NEW Fresh KOSHER Grocery Experience Has Arrived!

The Legacy Continues...
Stop In To See The NEW Carpathian Kosher Foods!

Kosher Grocery Shopping at it's Finest!
Come See The NEW & IMPROVED Carpathian Kosher Foods

No Pictures. Choose various color backgrounds and send me proofs. Think of other catchy phrases and provide examples. Don't only use the phrases I gave above.

The store was taken under new ownership and we want to promote the NEW and Improved Store.

Target Market(s)

Orthodox Jewish

Industry/Entity Type

Grocery Store

Requirements
Must have
• Logo
• Birchmont & Halvern in Skokie
Nice to have
• No Pictures.
Should not have
• Too much wording.

```html
<!DOCTYPE html>
<html lang="en">
<head>
<meta charset="utf-8">
<title>Carpathian Kosher Billboard</title>
<link rel="stylesheet" href="https://fonts.googleapis.com/css2?family=Montserrat:wght@700;800&family=Oswald:wght@700&display=swap">
<style>
  :root {
    --navy: #1b2447;
    --red: #e8202a;
    --yellow: #f2e91a;
    --white: #ffffff;
    --page: #ffffff;
  }
  * { margin: 0; padding: 0; box-sizing: border-box; }
  html, body {
    width: 1200px;
    height: 960px;
    overflow: hidden;
    background: var(--page);
  }
  .canvas {
    position: relative;
    width: 1200px;
    height: 960px;
  }
  .billboard {
    position: absolute;
    left: 30px;
    top: 430px;
    width: 1140px;
    height: 100px;
    background: var(--navy);
    overflow: hidden;
  }
  .brand-panel {
    position: absolute;
    left: 0;
    top: 0;
    width: 240px;
    height: 100px;
  }
  .brand-name {
    position: absolute;
    left: 16px;
    top: 50%;
    transform: translateY(-50%);
    display: flex;
    align-items: center;
    gap: 8px;
    font-family: "Montserrat", sans-serif;
    font-weight: 800;
    font-size: 17px;
    line-height: 1.1;
    color: var(--navy);
    text-transform: uppercase;
  }
  .brand-dot {
    width: 14px;
    height: 14px;
    border-radius: 50%;
    background: var(--red);
    flex: none;
  }
  .headline {
    position: absolute;
    left: 260px;
    width: 710px;
    top: 10px;
    text-align: center;
    font-family: "Montserrat", sans-serif;
    font-weight: 800;
    color: var(--white);
    letter-spacing: -0.5px;
  }
  .headline-main {
    font-size: 40px;
    line-height: 44px;
  }
  .headline-sub {
    font-size: 28px;
    line-height: 34px;
  }
  .red { color: var(--red); }
  .yellow { color: var(--yellow); }
  .location {
    position: absolute;
    right: 14px;
    top: 9px;
    width: 164px;
    height: 82px;
    background: var(--yellow);
    border-radius: 4px;
    display: flex;
    flex-direction: column;
    justify-content: center;
    align-items: center;
    font-family: "Oswald", sans-serif;
    font-weight: 700;
    font-size: 21px;
    line-height: 25px;
    color: var(--navy);
    text-align: center;
  }
</style>
</head>
<body>
<main class="canvas">
  <section class="billboard">
    <div class="brand-panel">
      <svg width="240" height="100" viewBox="0 0 240 100" aria-hidden="true">
        <path d="M0 0 H140 C158 30 175 65 190 100 H0 Z" fill="var(--white)"/>
        <path d="M140 0 H150 C168 30 185 65 200 100 H190 C175 65 158 30 140 0 Z" fill="var(--navy)"/>
        <path d="M150 0 H162 C180 30 197 65 212 100 H200 C185 65 168 30 150 0 Z" fill="var(--white)"/>
        <path d="M162 0 H178 C196 30 213 65 228 100 H212 C197 65 180 30 162 0 Z" fill="var(--red)"/>
      </svg>
      <div class="brand-name">
        <span class="brand-dot"></span>
        <span>Carpathian<br>Kosher</span>
      </div>
    </div>
    <h1 class="headline">
      <span class="headline-main">A <span class="red">NEW</span> <span class="yellow">Fresh</span> <span class="red">KOSHER</span></span><br>
      <span class="headline-sub">Grocery Experience Has <span class="yellow">Arrived!</span></span>
    </h1>
    <address class="location">
      <span class="red">Birchmont</span>
      <span>&amp; <span class="red">Halvern</span></span>
      <span>in Skokie</span>
    </address>
  </section>
</main>
</body>
</html>
```